**** Business card design for VoltaNode ****

For my ICT company VoltaNode I need I need a business card design.

We design, build and host web-applications and we have our own CMS product.

Some good examples are attached.

The information should be:
Joris Tielenburg
Managing director
E: j.tielenburg@voltanode-example.nl
M: +31(0)6 57218064
T: +31(0)40 7249305
W: www.voltanode-example.nl

Address:
Berend Vlootweg 27
5612 KT Eindhoven

Industry/Entity Type

Business

Requirements
Must have
• - Use logo (see attachments)
- Double sided
- Distinctive
Nice to have
• - Place for a statement on the back-side: "Designed with knowledge, built with passion"
- HTML code (or Wordpress)
- Dark (black or dark-gray) side
- Small simple images for telephone, e-mail en Url.
- QR code (only if not disturbing), not required, just an option

```html
<!DOCTYPE html>
<html lang="en">
<head>
<meta charset="utf-8">
<title>VoltaNode business card</title>
<link rel="stylesheet" href="https://fonts.googleapis.com/css2?family=Ubuntu:wght@400;500&display=swap">
<style>
  :root {
    --stage: #6f7071;
    --card-dark: #020306;
    --glow: #0f2a5c;
    --card-light: #ffffff;
    --pattern-light: #eef0f2;
    --brand-blue: #2f7fd6;
    --mark-blue: #2aa3e6;
    --tagline-blue: #2b6fd0;
    --ink: #1c1c1c;
    --muted: #6a6f75;
    --name-silver: #c9d2da;
  }
  * { box-sizing: border-box; margin: 0; padding: 0; }
  html, body {
    width: 1079px; height: 1200px; overflow: hidden;
    background: var(--stage);
    font-family: "Ubuntu", "Segoe UI", sans-serif;
  }
  .canvas { position: relative; width: 1079px; height: 1200px; }

  .card { position: absolute; left: 117px; width: 809px; height: 468px; overflow: hidden; }
  .card--front { top: 108px; background: var(--card-dark); }
  .card--back { top: 613px; background: var(--card-light); }

  .card__texture { position: absolute; inset: 0; }
  .card--front .card__texture {
    background: radial-gradient(ellipse 360px 300px at 230px 190px, var(--glow) 0%, rgba(8,20,48,0.6) 45%, transparent 80%);
  }
  .card--back .card__texture {
    background: linear-gradient(135deg, var(--pattern-light) 0%, #fafbfc 50%, var(--pattern-light) 100%);
  }

  .brand { position: absolute; display: flex; align-items: center; }
  .brand__dot { border-radius: 50%; background: var(--mark-blue); flex: none; }
  .brand__name { font-weight: 400; letter-spacing: 0.5px; line-height: 1; }

  .card--front .brand { left: 140px; top: 140px; }
  .card--front .brand__dot { width: 150px; height: 150px; margin-right: 36px; }
  .card--front .brand__name { font-size: 64px; color: var(--name-silver); }

  .tagline {
    position: absolute; left: 0; right: 0; top: 356px;
    text-align: center; font-size: 29px; color: var(--tagline-blue);
  }

  .card--back .brand { left: 420px; top: 56px; }
  .card--back .brand__dot { width: 110px; height: 110px; margin-right: 18px; }
  .card--back .brand__name { font-size: 46px; color: var(--mark-blue); }

  .person { position: absolute; left: 58px; top: 84px; }
  .person__name { font-size: 32px; color: var(--brand-blue); }
  .person__role { font-size: 28px; color: var(--muted); margin-top: 6px; }

  .contact { position: absolute; left: 56px; top: 286px; list-style: none; }
  .contact__item { display: flex; align-items: center; height: 35px; font-size: 23px; color: var(--ink); }
  .contact__icon { width: 22px; height: 22px; margin-right: 16px; fill: var(--ink); flex: none; }

  .address { position: absolute; left: 500px; top: 286px; font-size: 25px; line-height: 35px; color: var(--ink); font-style: normal; }
</style>
</head>
<body>
<main class="canvas">
  <section class="card card--front" aria-label="Card front">
    <div class="card__texture" role="img" aria-label="Dark circuit-maze background with a blue glow"></div>
    <div class="brand">
      <span class="brand__dot"></span>
      <span class="brand__name">VoltaNode</span>
    </div>
    <p class="tagline">Designed with knowledge, built with passion</p>
  </section>

  <section class="card card--back" aria-label="Card back">
    <div class="card__texture" role="img" aria-label="Faint light-grey maze pattern"></div>
    <div class="person">
      <p class="person__name">Joris Tielenburg</p>
      <p class="person__role">Managing director</p>
    </div>
    <div class="brand">
      <span class="brand__dot"></span>
      <span class="brand__name">VoltaNode</span>
    </div>
    <ul class="contact">
      <li class="contact__item">
        <svg class="contact__icon" viewBox="0 0 24 24" aria-hidden="true"><path d="M2 5h20v14H2z M3.5 6.5 12 13l8.5-6.5" fill="none" stroke="#1c1c1c" stroke-width="2"/></svg>
        j.tielenburg@voltanode-example.nl
      </li>
      <li class="contact__item">
        <svg class="contact__icon" viewBox="0 0 24 24" aria-hidden="true"><rect x="6" y="1" width="12" height="22" rx="2"/><rect x="8" y="4" width="8" height="9" fill="#fff"/><rect x="8" y="15" width="8" height="5" fill="#fff"/></svg>
        +31(0)6 57218064
      </li>
      <li class="contact__item">
        <svg class="contact__icon" viewBox="0 0 24 24" aria-hidden="true"><path d="M2 9c0-3 4-5 10-5s10 2 10 5v2h-5V9H7v2H2z"/><path d="M5 13h14l2 8H3z"/><circle cx="12" cy="17" r="2" fill="#fff"/></svg>
        +31(0)40 7249305
      </li>
      <li class="contact__item">
        <svg class="contact__icon" viewBox="0 0 24 24" aria-hidden="true"><circle cx="12" cy="12" r="11"/><path d="M1 12h22M12 1c4 4 4 18 0 22M12 1c-4 4-4 18 0 22" fill="none" stroke="#fff" stroke-width="1.5"/></svg>
        www.voltanode-example.nl
      </li>
    </ul>
    <address class="address">
      Berend Vlootweg 27<br>
      5612 KT Eindhoven
    </address>
  </section>
</main>
</body>
</html>
```